Marlow Crest LLC PowerPoint Template

I recently formed an LLC for my independent consulting work. I need a very professional looking Powerpoint template to use for client presentations and proposals.

Target Market(s)

Small to Mid Size businesses in all industries

Industry/Entity Type

Consulting

Requirements
Must have
• Contemporary and tech feel

```html
<!DOCTYPE html>
<html lang="en">
<head>
<meta charset="utf-8">
<title>Marlow Crest LLC – Presentation Template</title>
<link rel="stylesheet" href="https://fonts.googleapis.com/css2?family=Bebas+Neue&family=Roboto:wght@400;500;700&display=swap">
<style>
:root{
  --canvas:#a6a6a6;
  --ink:#1b2440;
  --text:#333845;
  --deep:#1f3a9a;
  --blue:#1565d8;
  --bright:#1a9ee9;
  --line:#c9cfdc;
  --soft:#e9edf4;
  --cell:#dedede;
  --cell-alt:#ececec;
  --white:#ffffff;
}
*{box-sizing:border-box;margin:0;padding:0}
html,body{width:1200px;height:2647px;overflow:hidden;background:var(--canvas)}
body{position:relative;font-family:'Roboto',Arial,sans-serif;color:var(--text)}
.slide{position:absolute;width:515px;height:296px;overflow:hidden;background:var(--white)}
.col-l{left:64px}.col-r{left:623px}
.r1{top:61px}.r2{top:379px}.r3{top:698px}.r4{top:1016px}.r5{top:1335px}.r6{top:1653px}.r7{top:1972px}.r8{top:2290px}
.abs{position:absolute}
.gfx{position:absolute;left:0;top:0;width:515px;height:296px}
.title{position:absolute;left:18px;top:15px;padding-left:13px;font:21px/1 'Bebas Neue',sans-serif;color:var(--ink);letter-spacing:.3px}
.title::before{content:"";position:absolute;left:0;top:2px;width:7px;height:7px;background:var(--blue)}
.foot-line{position:absolute;left:18px;right:18px;top:253px;height:1px;background:var(--line)}
.brand{position:absolute;left:18px;top:263px;font:13px/1 'Bebas Neue',sans-serif;color:var(--blue);display:flex;align-items:center;gap:4px}
.brand::before{content:"";width:7px;height:7px;border-radius:50%;background:var(--blue)}
.page{position:absolute;right:18px;top:263px;width:15px;height:15px;background:var(--blue);color:#fff;font:700 8px/15px 'Roboto',sans-serif;text-align:center}
.tiny{font-size:6.6px;line-height:1.3;color:var(--text)}
.center{text-align:center}
.para{position:absolute;left:30px;width:455px;font-size:6.6px;line-height:1.32;text-align:center;color:var(--text)}
.h-item{font:700 9px/1.1 'Roboto',sans-serif;color:var(--ink)}
.pill{display:inline-block;background:var(--blue);color:#fff;font:700 8px/1 'Roboto',sans-serif;padding:2px 9px;border-radius:8px}
.photo{position:absolute;background:linear-gradient(135deg,#6f86a8 0%,#3a5482 45%,#c9d3e0 100%)}
/* covers */
.cover{background:linear-gradient(120deg,#1d3597 0%,#1b5fd0 55%,#1aa3ec 100%)}
.cover-brand{position:absolute;font:22px/1 'Bebas Neue',sans-serif;color:#fff;display:flex;align-items:center;gap:6px}
.cover-brand::before{content:"";width:10px;height:10px;border-radius:50%;background:#fff}
.cover-head{position:absolute;font:42px/0.95 'Bebas Neue',sans-serif;color:#fff}
.web{position:absolute;display:flex;align-items:center;gap:4px;font:500 9.5px/1 'Roboto',sans-serif;color:#fff}
.web-pill{background:#fff;color:var(--ink);border-radius:11px;padding:4px 10px}
/* services */
.svc{position:absolute;width:190px}
.svc .h-item{margin-bottom:2px}
/* tables */
.price{position:absolute;left:71px;display:flex;gap:6px}
.pcol{display:flex;flex-direction:column;gap:1px}
.pcol .th{height:17px;border-radius:6px 6px 0 0;background:linear-gradient(90deg,var(--deep),var(--bright));color:#fff;font:700 6.4px/17px 'Roboto',sans-serif;text-align:center}
.pcol .td{height:15px;background:var(--cell);font:6.4px/15px 'Roboto',sans-serif;text-align:center;color:#222}
.pcol .td:nth-child(odd){background:var(--cell-alt)}
/* cards */
.card{position:absolute;top:61px;width:142px;height:159px;border:1px solid var(--blue);border-radius:7px;overflow:hidden}
.card .ch{height:21px;background:linear-gradient(90deg,var(--deep),var(--bright));color:#fff;font:700 7px/21px 'Roboto',sans-serif;text-align:center}
.card ul{list-style:none;padding:6px 6px 0 8px}
.card li{position:relative;padding-left:10px;margin-bottom:7px;font-size:6.3px;line-height:1.28}
.card li::before{content:"";position:absolute;left:0;top:1px;width:5px;height:5px;border-radius:50%;background:var(--blue)}
/* location */
.loc{position:absolute;left:387px;width:69px;height:11px;border-radius:6px;background:var(--deep);color:#fff;font:500 6.6px/11px 'Roboto',sans-serif;text-align:center}
/* contact */
.c-item{position:absolute;display:flex;align-items:center;gap:6px}
.c-icon{width:26px;height:26px;border-radius:50%;background:linear-gradient(135deg,var(--deep),var(--bright));border:2px solid #fff;box-shadow:0 0 0 1px #c8d6f0;display:flex;align-items:center;justify-content:center}
.c-text b{display:block;font:700 9px/1.1 'Roboto',sans-serif;color:var(--ink)}
.c-text span{font-size:6.8px;color:var(--text)}
.dark .c-text b,.dark .c-text span{color:#fff}
.disclaimer h2{position:absolute;left:0;right:0;top:56px;text-align:center;font:100px/1 'Bebas Neue',sans-serif;color:#fff;letter-spacing:2px}
.disclaimer p{position:absolute;left:34px;width:447px;font-size:6.4px;line-height:1.3;text-align:center;color:#fff}
</style>
</head>
<body>

<svg width="0" height="0" style="position:absolute" aria-hidden="true">
  <defs>
    <linearGradient id="g-blue" x1="0" y1="0" x2="1" y2="1"><stop offset="0" stop-color="#1f3a9a"/><stop offset="1" stop-color="#1a9ee9"/></linearGradient>
    <linearGradient id="g-blue-h" x1="0" y1="0" x2="1" y2="0"><stop offset="0" stop-color="#1f3a9a"/><stop offset="1" stop-color="#1a9ee9"/></linearGradient>
    <symbol id="i-case" viewBox="0 0 24 24"><rect x="2" y="7" width="20" height="13" rx="2" fill="currentColor"/><path d="M9 7V5h6v2" fill="none" stroke="currentColor" stroke-width="2"/><rect x="2" y="12" width="20" height="1.5" fill="#1f50b8"/><rect x="10.5" y="11" width="3" height="3.5" fill="currentColor"/></symbol>
    <symbol id="i-bulb" viewBox="0 0 24 24"><circle cx="12" cy="11" r="5" fill="none" stroke="currentColor" stroke-width="1.8"/><rect x="10" y="16.5" width="4" height="3" fill="currentColor"/><path d="M12 2v2M4 11H2M22 11h-2M5.5 4.5l1.4 1.4M18.5 4.5l-1.4 1.4" stroke="currentColor" stroke-width="1.6"/></symbol>
    <symbol id="i-target" viewBox="0 0 24 24"><circle cx="12" cy="12" r="9" fill="none" stroke="currentColor" stroke-width="1.8"/><circle cx="12" cy="12" r="5" fill="none" stroke="currentColor" stroke-width="1.8"/><circle cx="12" cy="12" r="1.6" fill="currentColor"/><path d="M12 12l8-8M17 4h3v3" stroke="currentColor" stroke-width="1.8" fill="none"/></symbol>
    <symbol id="i-pin" viewBox="0 0 24 24"><path d="M12 2a7 7 0 0 0-7 7c0 5 7 13 7 13s7-8 7-13a7 7 0 0 0-7-7z" fill="currentColor"/><circle cx="12" cy="9" r="2.6" fill="#fff"/></symbol>
    <symbol id="i-phone" viewBox="0 0 24 24"><path d="M6 3l3 0 2 5-2 1.5c1 2.5 3 4.5 5.5 5.5L16 13l5 2v3c0 1.5-1.5 3-3 3C10 21 3 14 3 6c0-1.5 1.5-3 3-3z" fill="currentColor"/></symbol>
    <symbol id="i-mail" viewBox="0 0 24 24"><rect x="2" y="5" width="20" height="14" rx="1.5" fill="currentColor"/><path d="M3 6l9 7 9-7" fill="none" stroke="#1f50b8" stroke-width="1.6"/></symbol>
    <symbol id="i-screen" viewBox="0 0 24 24"><rect x="2" y="4" width="20" height="13" rx="1.5" fill="none" stroke="currentColor" stroke-width="2"/><path d="M8 21h8M12 17v4" stroke="currentColor" stroke-width="2"/></symbol>
    <symbol id="i-globe" viewBox="0 0 24 24"><circle cx="12" cy="12" r="9.5" fill="none" stroke="currentColor" stroke-width="1.8"/><ellipse cx="12" cy="12" rx="4" ry="9.5" fill="none" stroke="currentColor" stroke-width="1.6"/><path d="M2.5 12h19M4 7h16M4 17h16" stroke="currentColor" stroke-width="1.4"/></symbol>
    <symbol id="i-rocket" viewBox="0 0 24 24"><path d="M14 3c4 0 7 3 7 7l-8 8-7-7 8-8z" fill="currentColor"/><circle cx="15" cy="9" r="2" fill="#fff"/><path d="M6 11l-3 1 3-5 4 0M13 18l-1 3 5-3 0-4" fill="currentColor"/><path d="M5 16l-2 5 5-2" fill="none" stroke="currentColor" stroke-width="1.5"/></symbol>
    <symbol id="i-list" viewBox="0 0 24 24"><rect x="4" y="2" width="16" height="20" rx="1.5" fill="none" stroke="currentColor" stroke-width="1.8"/><path d="M7 7h2M11 7h6M7 11h2M11 11h6M7 15h2M11 15h6M7 19h2M11 19h6" stroke="currentColor" stroke-width="1.5"/></symbol>
    <marker id="arrow" viewBox="0 0 10 10" refX="8" refY="5" markerWidth="6" markerHeight="6" orient="auto"><path d="M0 0L10 5L0 10z" fill="#1f50b8"/></marker>
  </defs>
</svg>

<!-- Cover A -->
<section class="slide cover col-l r1">
  <div class="photo" role="img" aria-label="Business team meeting in a modern office, toned blue" style="left:0;top:0;width:515px;height:296px;opacity:.25;background:linear-gradient(160deg,#9db4d6,#2a4f9a 60%,#1a7fd8)"></div>
  <div class="cover-brand" style="left:20px;top:68px">MARLOW CREST LLC</div>
  <h1 class="cover-head" style="left:20px;top:115px">HEADING GOES<br>HERE</h1>
  <div class="web" style="left:20px;top:221px"><svg width="12" height="12" style="color:#fff"><use href="#i-globe"/></svg>www.marlowcrest.com</div>
</section>

<!-- Cover B -->
<section class="slide cover col-r r1">
  <div class="abs" style="left:0;top:0;width:515px;height:296px;background:#fff;clip-path:polygon(76% 0,100% 0,100% 100%,88% 100%)"></div>
  <h1 class="cover-head" style="left:18px;top:70px;font-size:54px">HEADING<br>GOES HERE</h1>
  <div class="web web-pill" style="left:18px;top:187px"><svg width="12" height="12" style="color:var(--ink)"><use href="#i-globe"/></svg>www.marlowcrest.com</div>
  <div class="abs" style="left:233px;top:17px;width:216px;height:216px;border-radius:50%;background:#fff;border:14px solid var(--blue);display:flex;flex-direction:column;align-items:center;justify-content:center">
    <div style="font:36px/1 'Bebas Neue',sans-serif;color:var(--blue)">MARLOW CREST</div>
    <div style="font:14px/1.2 'Bebas Neue',sans-serif;color:var(--blue);letter-spacing:4px">LLC</div>
  </div>
</section>

<!-- About Us -->
<section class="slide col-l r2">
  <h2 class="title">About Us</h2>
  <div class="photo" role="img" aria-label="Consultant presenting charts to a team around a meeting table" style="left:32px;top:53px;width:451px;height:130px"></div>
  <p class="para" style="top:191px">Lorem Ipsum is simply dummy text of the printing and typesetting industry. Lorem Ipsum has been the industry's standard dummy text ever since the 1500s, when an unknown printer took a galley of type and scrambled it to make a type specimen book. It has survived not only five centuries, but also the leap into electronic typesetting, remaining essentially unchanged. It was popularised in the 1960s with the release of Letraset sheets containing Lorem Ipsum passages, and more recently with desktop publishing software like Aldus PageMaker including versions of Lorem Ipsum.</p>
  <div class="foot-line"></div><div class="brand">Marlow Crest LLC</div><div class="page">2</div>
</section>

<!-- Our Mission -->
<section class="slide col-r r2">
  <h2 class="title">Our Mission</h2>
  <svg class="gfx" viewBox="0 0 515 296">
    <path d="M34 112H484" stroke="#1f50b8" stroke-width="1.2"/>
    <path d="M34 112l6-3.5v7z M484 112l-6-3.5v7z" fill="#1f50b8"/>
    <circle cx="178" cy="112" r="27" fill="url(#g-blue)"/>
    <circle cx="257" cy="112" r="40" fill="url(#g-blue)"/>
    <circle cx="336" cy="112" r="27" fill="url(#g-blue)"/>
    <use href="#i-bulb" x="166" y="100" width="24" height="24" style="color:#fff"/>
    <use href="#i-case" x="238" y="93" width="38" height="38" style="color:#fff"/>
    <use href="#i-target" x="324" y="100" width="24" height="24" style="color:#fff"/>
  </svg>
  <p class="para" style="top:162px">Lorem Ipsum is simply dummy text of the printing and typesetting industry. Lorem Ipsum has been the industry's standard dummy text ever since the 1500s, when an unknown printer took a galley of type and scrambled it to make a type specimen book. It has survived not only five centuries, but also the leap into electronic typesetting, remaining essentially unchanged. It was popularised in the 1960s with the release of Letraset sheets containing Lorem Ipsum passages, and more recently with desktop publishing software like Aldus PageMaker including versions of Lorem Ipsum.</p>
  <div class="foot-line"></div><div class="brand">Marlow Crest LLC</div><div class="page">3</div>
</section>

<!-- Our History -->
<section class="slide col-l r3">
  <h2 class="title">Our History</h2>
  <svg class="gfx" viewBox="0 0 515 296">
    <rect x="18" y="149" width="479" height="3" fill="#d5d9e2"/>
    <g fill="url(#g-blue-h)">
      <rect x="30" y="149" width="84" height="3"/><rect x="124" y="149" width="84" height="3"/><rect x="217" y="149" width="84" height="3"/><rect x="311" y="149" width="84" height="3"/><rect x="404" y="149" width="84" height="3"/>
    </g>
    <g stroke="#1f50b8" stroke-width="1" stroke-dasharray="2 2">
      <path d="M71 104V148M164 104V148M257 104V148M351 104V148M444 104V148"/>
    </g>
    <g fill="url(#g-blue)"><circle cx="71" cy="95" r="9"/><circle cx="164" cy="95" r="9"/><circle cx="257" cy="95" r="9"/><circle cx="351" cy="95" r="9"/><circle cx="444" cy="95" r="9"/></g>
    <g style="color:#fff"><use href="#i-bulb" x="65" y="89" width="12" height="12"/><use href="#i-bulb" x="158" y="89" width="12" height="12"/><use href="#i-bulb" x="251" y="89" width="12" height="12"/><use href="#i-bulb" x="345" y="89" width="12" height="12"/><use href="#i-bulb" x="438" y="89" width="12" height="12"/></g>
  </svg>
  <p class="abs tiny center" style="left:31px;top:157px;width:80px">Lorem Ipsum is simply dummy text of the printing and typesetting industry.</p>
  <p class="abs tiny center" style="left:124px;top:157px;width:80px">Lorem Ipsum is simply dummy text of the printing and typesetting industry.</p>
  <p class="abs tiny center" style="left:217px;top:157px;width:80px">Lorem Ipsum is simply dummy text of the printing and typesetting industry.</p>
  <p class="abs tiny center" style="left:311px;top:157px;width:80px">Lorem Ipsum is simply dummy text of the printing and typesetting industry.</p>
  <p class="abs tiny center" style="left:404px;top:157px;width:80px">Lorem Ipsum is simply dummy text of the printing and typesetting industry.</p>
  <div class="foot-line"></div><div class="brand">Marlow Crest LLC</div><div class="page">4</div>
</section>

<!-- Our Services -->
<section class="slide col-r r3">
  <h2 class="title">Our Services</h2>
  <svg class="gfx" viewBox="0 0 515 296">
    <path d="M258 57V230" stroke="#c9cfdc"/><path d="M30 143H242M274 143H484" stroke="#c9cfdc"/>
    <g fill="url(#g-blue)"><circle cx="72" cy="93" r="32"/><circle cx="310" cy="93" r="32"/><circle cx="72" cy="192" r="32"/><circle cx="310" cy="192" r="32"/></g>
    <g style="color:#fff"><use href="#i-case" x="55" y="76" width="34" height="34"/><use href="#i-case" x="293" y="76" width="34" height="34"/><use href="#i-case" x="55" y="175" width="34" height="34"/><use href="#i-case" x="293" y="175" width="34" height="34"/></g>
  </svg>
  <div class="svc" style="left:112px;top:69px"><div class="h-item">Title Here</div><p class="tiny">Lorem Ipsum is simply dummy text of the printing and typesetting industry. Lorem Ipsum has been the industry's standard.</p></div>
  <div class="svc" style="left:350px;top:69px;width:130px"><div class="h-item">Title Here</div><p class="tiny">Lorem Ipsum is simply dummy text of the printing and typesetting industry. Lorem Ipsum has been the industry's standard.</p></div>
  <div class="svc" style="left:112px;top:168px;width:130px"><div class="h-item">Title Here</div><p class="tiny">Lorem Ipsum is simply dummy text of the printing and typesetting industry. Lorem Ipsum has been the industry's standard.</p></div>
  <div class="svc" style="left:350px;top:168px;width:130px"><div class="h-item">Title Here</div><p class="tiny">Lorem Ipsum is simply dummy text of the printing and typesetting industry. Lorem Ipsum has been the industry's standard.</p></div>
  <div class="foot-line"></div><div class="brand">Marlow Crest LLC</div><div class="page">5</div>
</section>

<!-- Our Team -->
<section class="slide col-l r4">
  <h2 class="title">Our Team</h2>
  <div class="photo" role="img" aria-label="Portrait of a team member" style="left:31px;top:56px;width:126px;height:126px;border-radius:50%;border:3px solid #fff;box-shadow:0 0 0 2px var(--blue)"></div>
  <div class="photo" role="img" aria-label="Portrait of a team member" style="left:194px;top:56px;width:126px;height:126px;border-radius:50%;border:3px solid #fff;box-shadow:0 0 0 2px var(--blue)"></div>
  <div class="photo" role="img" aria-label="Portrait of a team member" style="left:357px;top:56px;width:126px;height:126px;border-radius:50%;border:3px solid #fff;box-shadow:0 0 0 2px var(--blue)"></div>
  <div class="abs center" style="left:29px;top:194px;width:130px"><div class="h-item">Name Here</div><p class="tiny">Lorem Ipsum is simply dummy text of the printing and typesetting industry.</p></div>
  <div class="abs center" style="left:192px;top:194px;width:130px"><div class="h-item">Name Here</div><p class="tiny">Lorem Ipsum is simply dummy text of the printing and typesetting industry.</p></div>
  <div class="abs center" style="left:355px;top:194px;width:130px"><div class="h-item">Name Here</div><p class="tiny">Lorem Ipsum is simply dummy text of the printing and typesetting industry.</p></div>
  <div class="foot-line"></div><div class="brand">Marlow Crest LLC</div><div class="page">6</div>
</section>

<!-- Our Process (cycle) -->
<section class="slide col-r r4">
  <h2 class="title">Our Process</h2>
  <svg class="gfx" viewBox="0 0 515 296">
    <g fill="none" stroke="#1f50b8" stroke-width="1.2" marker-end="url(#arrow)">
      <path d="M205 120 Q212 98 231 88"/>
      <path d="M283 88 Q302 98 309 116"/>
      <path d="M309 168 Q302 186 283 196"/>
      <path d="M231 196 Q212 186 205 168"/>
    </g>
    <g fill="url(#g-blue)"><circle cx="257" cy="80" r="18"/><circle cx="320" cy="142" r="18"/><circle cx="257" cy="204" r="18"/><circle cx="194" cy="142" r="18"/></g>
    <g style="color:#fff"><use href="#i-bulb" x="247" y="70" width="20" height="20"/><use href="#i-case" x="310" y="132" width="20" height="20"/><use href="#i-bulb" x="247" y="194" width="20" height="20"/><use href="#i-target" x="184" y="132" width="20" height="20"/></g>
  </svg>
  <div class="abs center" style="left:222px;top:134px;width:70px;font:13px/1 'Bebas Neue',sans-serif;color:var(--blue)">Marlow Crest</div>
  <div class="abs center" style="left:107px;top:37px;width:300px"><div class="h-item">Step One</div><p class="tiny">Lorem Ipsum is simply dummy text of the printing and typesetting industry.</p></div>
  <div class="abs" style="left:345px;top:121px;width:110px"><div class="h-item">Step Two</div><p class="tiny">Lorem Ipsum is simply dummy text of the printing and typesetting industry.</p></div>
  <div class="abs" style="left:62px;top:121px;width:110px;text-align:right"><div class="h-item">Step Four</div><p class="tiny">Lorem Ipsum is simply dummy text of the printing and typesetting industry.</p></div>
  <div class="abs center" style="left:107px;top:226px;width:300px"><div class="h-item">Step Three</div><p class="tiny">Lorem Ipsum is simply dummy text of the printing and typesetting industry.</p></div>
  <div class="foot-line"></div><div class="brand">Marlow Crest LLC</div><div class="page">7</div>
</section>

<!-- Pie Chart -->
<section class="slide col-l r5">
  <h2 class="title">Pie Chart</h2>
  <svg class="gfx" viewBox="0 0 515 296">
    <g transform="rotate(-90 257 138)" fill="none" stroke-width="50">
      <circle cx="257" cy="138" r="43" stroke="#1a7fe0" stroke-dasharray="54.04 270.18"/>
      <circle cx="257" cy="138" r="43" stroke="#1874de" stroke-dasharray="135.09 270.18" stroke-dashoffset="-54.04"/>
      <circle cx="257" cy="138" r="43" stroke="#1f3a9a" stroke-dasharray="54.04 270.18" stroke-dashoffset="-189.13"/>
      <circle cx="257" cy="138" r="43" stroke="#2250b8" stroke-dasharray="27.02 270.18" stroke-dashoffset="-243.17"/>
    </g>
    <g stroke="#fff" stroke-width="1.2"><path d="M257 138V70M257 138L321.7 117M257 138L217 193M257 138L192.3 117M257 138L236 73.3"/></g>
    <circle cx="257" cy="138" r="18" fill="#fff"/>
    <g fill="#fff" font-family="Roboto,sans-serif" font-weight="700" font-size="11" text-anchor="middle">
      <text x="290" y="110">20%</text><text x="278" y="183">50%</text><text x="214" y="140">20%</text><text x="238" y="98">10%</text>
    </g>
    <g fill="none" stroke="#1f50b8" stroke-width="0.8">
      <path d="M180 71H220L234 82"/><path d="M148 141H198"/><path d="M320 89H350"/><path d="M306 188L316 197H350"/>
    </g>
  </svg>
  <div class="abs" style="left:117px;top:65px"><span class="pill">Title Here</span></div>
  <p class="abs tiny center" style="left:40px;top:79px;width:135px">Lorem Ipsum is simply dummy text of the printing and typesetting industry.</p>
  <div class="abs" style="left:82px;top:135px"><span class="pill">Title Here</span></div>
  <p class="abs tiny center" style="left:35px;top:149px;width:110px">Lorem Ipsum is simply dummy text of the printing and typesetting industry.</p>
  <div class="abs" style="left:350px;top:83px"><span class="pill">Title Here</span></div>
  <p class="abs tiny" style="left:362px;top:97px;width:110px">Lorem Ipsum is simply dummy text of the printing and typesetting industry.</p>
  <div class="abs" style="left:350px;top:193px"><span class="pill">Title Here</span></div>
  <p class="abs tiny" style="left:362px;top:207px;width:135px">Lorem Ipsum is simply dummy text of the printing and typesetting industry.</p>
  <div class="foot-line"></div><div class="brand">Marlow Crest LLC</div><div class="page">8</div>
</section>

<!-- Our Process (steps) -->
<section class="slide col-r r5">
  <h2 class="title">Our Process</h2>
  <svg class="gfx" viewBox="0 0 515 296">
    <g fill="none" stroke="url(#g-blue)">
      <circle cx="100" cy="141" r="52" stroke-width="1.2"/><circle cx="256" cy="141" r="52" stroke-width="1.2"/><circle cx="412" cy="141" r="52" stroke-width="1.2"/>
      <path d="M104 76A65 65 0 0 1 104 206" stroke-width="5"/><path d="M260 76A65 65 0 0 1 260 206" stroke-width="5"/><path d="M416 76A65 65 0 0 1 416 206" stroke-width="5"/>
    </g>
    <g fill="#1a8be6"><path d="M169 134l7 7-7 7z"/><path d="M325 134l7 7-7 7z"/><path d="M481 134l7 7-7 7z"/></g>
    <g fill="url(#g-blue)"><circle cx="45" cy="141" r="11"/><circle cx="201" cy="141" r="11"/><circle cx="357" cy="141" r="11"/></g>
    <g fill="#fff" font-family="Roboto,sans-serif" font-weight="700" font-size="9" text-anchor="middle"><text x="45" y="144.5">01</text><text x="201" y="144.5">02</text><text x="357" y="144.5">03</text></g>
    <g style="color:#1f50b8"><use href="#i-rocket" x="89" y="95" width="22" height="22"/><use href="#i-list" x="245" y="95" width="22" height="22"/><use href="#i-case" x="401" y="95" width="22" height="22"/></g>
  </svg>
  <p class="abs tiny center" style="left:64px;top:135px;width:76px">Lorem Ipsum is simply dummy text of the printing and typesetting industry.</p>
  <p class="abs tiny center" style="left:220px;top:135px;width:76px">Lorem Ipsum is simply dummy text of the printing and typesetting industry.</p>
  <p class="abs tiny center" style="left:376px;top:135px;width:76px">Lorem Ipsum is simply dummy text of the printing and typesetting industry.</p>
  <div class="foot-line"></div><div class="brand">Marlow Crest LLC</div><div class="page">9</div>
</section>

<!-- Price List -->
<section class="slide col-l r6">
  <h2 class="title">Price List</h2>
  <div class="price" style="top:51px">
    <div class="pcol" style="width:119px"><div class="th">TITLE HERE</div><div class="td">Year 1</div><div class="td">Year 2</div><div class="td">Year 3</div><div class="td">Year 4</div></div>
    <div class="pcol" style="width:69px"><div class="th">TITLE HERE</div><div class="td">9,999</div><div class="td">10,999</div><div class="td">11,999</div><div class="td">12,999</div></div>
    <div class="pcol" style="width:68px"><div class="th">TITLE HERE</div><div class="td">6%</div><div class="td">6%</div><div class="td">6%</div><div class="td">6%</div></div>
    <div class="pcol" style="width:94px"><div class="th">TITLE HERE</div><div class="td">9,999</div><div class="td">10,999</div><div class="td">11,999</div><div class="td">12,999</div></div>
  </div>
  <div class="price" style="top:151px">
    <div class="pcol" style="width:119px"><div class="th">TITLE HERE</div><div class="td">Year 1</div><div class="td">Year 2</div><div class="td">Year 3</div><div class="td">Year 4</div></div>
    <div class="pcol" style="width:69px"><div class="th">TITLE HERE</div><div class="td">9,999</div><div class="td">10,999</div><div class="td">11,999</div><div class="td">12,999</div></div>
    <div class="pcol" style="width:68px"><div class="th">TITLE HERE</div><div class="td">9%</div><div class="td">9%</div><div class="td">9%</div><div class="td">9%</div></div>
    <div class="pcol" style="width:94px"><div class="th">TITLE HERE</div><div class="td">9,999</div><div class="td">10,999</div><div class="td">11,999</div><div class="td">12,999</div></div>
  </div>
  <div class="foot-line"></div><div class="brand">Marlow Crest LLC</div><div class="page">10</div>
</section>

<!-- Heading Goes Here (cards) -->
<section class="slide col-r r6">
  <h2 class="title">Heading Goes Here</h2>
  <div class="card" style="left:31px"><div class="ch">TITLE HERE</div><ul>
    <li>Lorem Ipsum is simply dummy text of the printing and typesetting industry. Lorem Ipsum has been the industry's standard.</li>
    <li>Lorem Ipsum is simply dummy text of the printing and typesetting industry. Lorem Ipsum has been the industry's standard.</li>
    <li>Lorem Ipsum is simply dummy text of the printing and typesetting industry. Lorem Ipsum has been the industry's standard.</li></ul></div>
  <div class="card" style="left:186px"><div class="ch">TITLE HERE</div><ul>
    <li>Lorem Ipsum is simply dummy text of the printing and typesetting industry. Lorem Ipsum has been the industry's standard.</li>
    <li>Lorem Ipsum is simply dummy text of the printing and typesetting industry. Lorem Ipsum has been the industry's standard.</li>
    <li>Lorem Ipsum is simply dummy text of the printing and typesetting industry. Lorem Ipsum has been the industry's standard.</li></ul></div>
  <div class="card" style="left:341px"><div class="ch">TITLE HERE</div><ul>
    <li>Lorem Ipsum is simply dummy text of the printing and typesetting industry. Lorem Ipsum has been the industry's standard.</li>
    <li>Lorem Ipsum is simply dummy text of the printing and typesetting industry. Lorem Ipsum has been the industry's standard.</li>
    <li>Lorem Ipsum is simply dummy text of the printing and typesetting industry. Lorem Ipsum has been the industry's standard.</li></ul></div>
  <div class="foot-line"></div><div class="brand">Marlow Crest LLC</div><div class="page">11</div>
</section>

<!-- Office Location -->
<section class="slide col-l r7">
  <h2 class="title">Our Office Location</h2>
  <div class="abs" role="img" aria-label="World map with office locations" style="left:45px;top:58px;width:290px;height:170px;background:#dcdcdc;border-radius:40px 60px 50px 70px"></div>
  <svg class="gfx" viewBox="0 0 515 296" style="color:var(--blue)">
    <use href="#i-pin" x="152" y="65" width="14" height="14"/>
    <use href="#i-pin" x="95" y="100" width="14" height="14"/>
    <use href="#i-pin" x="266" y="107" width="14" height="14"/>
    <use href="#i-pin" x="202" y="145" width="14" height="14"/>
    <use href="#i-pin" x="136" y="169" width="14" height="14"/>
    <use href="#i-pin" x="305" y="191" width="14" height="14"/>
  </svg>
  <div class="loc" style="top:94px">Location One</div>
  <div class="loc" style="top:115px">Location Two</div>
  <div class="loc" style="top:136px">Location Three</div>
  <div class="loc" style="top:157px">Location Four</div>
  <div class="loc" style="top:178px">Location Five</div>
  <div class="loc" style="top:199px">Location Six</div>
  <div class="foot-line"></div><div class="brand">Marlow Crest LLC</div><div class="page">12</div>
</section>

<!-- Disclaimer -->
<section class="slide cover disclaimer col-r r7">
  <h2>DISCLAIMER</h2>
  <p style="top:154px">Lorem Ipsum is simply dummy text of the printing and typesetting industry. Lorem Ipsum has been the industry's standard dummy text ever since the 1500s, when an unknown printer took a galley of type and scrambled it to make a type specimen book. It has survived not only five centuries, but also the leap into electronic typesetting, remaining essentially unchanged. It was popularised in the 1960s with the release of Letraset sheets containing Lorem Ipsum passages, and more recently with desktop publishing software like Aldus PageMaker including versions of Lorem Ipsum. Lorem Ipsum is simply dummy text of the printing and typesetting industry.</p>
  <p style="top:203px">Lorem Ipsum has been the industry's standard dummy text ever since the 1500s, when an unknown printer took a galley of type and scrambled it to make a type specimen book. It has survived not only five centuries, but also the leap into electronic typesetting, remaining essentially unchanged. It was popularised in the 1960s with the release of Letraset sheets containing Lorem Ipsum passages, and more recently with desktop publishing software like Aldus PageMaker including versions of Lorem Ipsum.</p>
</section>

<!-- Contact Us -->
<section class="slide col-l r8">
  <h2 class="title">Contact Us</h2>
  <div class="photo" role="img" aria-label="Team of consultants working at a conference table" style="left:100px;top:53px;width:172px;height:172px;border-radius:50%"></div>
  <div class="c-item" style="left:254px;top:70px"><div class="c-icon"><svg width="14" height="14" style="color:#fff"><use href="#i-pin"/></svg></div><div class="c-text"><b>Address</b><span>Lorem Ipsum is simply dummy</span></div></div>
  <div class="c-item" style="left:270px;top:109px"><div class="c-icon"><svg width="13" height="13" style="color:#fff"><use href="#i-phone"/></svg></div><div class="c-text"><b>Phone</b><span>Lorem Ipsum is simply dummy</span></div></div>
  <div class="c-item" style="left:270px;top:149px"><div class="c-icon"><svg width="13" height="13" style="color:#fff"><use href="#i-mail"/></svg></div><div class="c-text"><b>Email</b><span>Lorem Ipsum is simply dummy</span></div></div>
  <div class="c-item" style="left:254px;top:188px"><div class="c-icon"><svg width="13" height="13" style="color:#fff"><use href="#i-screen"/></svg></div><div class="c-text"><b>Website</b><span>Lorem Ipsum is simply dummy</span></div></div>
  <div class="foot-line"></div><div class="brand">Marlow Crest LLC</div><div class="page">14</div>
</section>

<!-- Contact (closing) -->
<section class="slide cover dark col-r r8" style="background:linear-gradient(120deg,#1a8fe6 0%,#1b5fd0 45%,#1f3597 100%)">
  <div class="photo" role="img" aria-label="Team of consultants working at a conference table" style="left:69px;top:25px;width:230px;height:230px;border-radius:50%"></div>
  <div class="c-item" style="left:281px;top:74px"><div class="c-icon"><svg width="14" height="14" style="color:#fff"><use href="#i-pin"/></svg></div><div class="c-text"><b>Address</b><span>Lorem Ipsum is simply dummy</span></div></div>
  <div class="c-item" style="left:297px;top:114px"><div class="c-icon"><svg width="13" height="13" style="color:#fff"><use href="#i-phone"/></svg></div><div class="c-text"><b>Phone</b><span>Lorem Ipsum is simply dummy</span></div></div>
  <div class="c-item" style="left:297px;top:154px"><div class="c-icon"><svg width="13" height="13" style="color:#fff"><use href="#i-mail"/></svg></div><div class="c-text"><b>Email</b><span>Lorem Ipsum is simply dummy</span></div></div>
  <div class="c-item" style="left:281px;top:193px"><div class="c-icon"><svg width="13" height="13" style="color:#fff"><use href="#i-screen"/></svg></div><div class="c-text"><b>Website</b><span>Lorem Ipsum is simply dummy</span></div></div>
</section>

</body>
</html>
```